BramliVex a new start up looking for packaging design for it's organic Cold pressed Peanut oil.

We require a labelling design for a new company based in the UK called ''BramliVex''. We will be launching Organic cold pressed peanut oil. We would like a design that is simple yet very catchy and not boring.

Target Market(s)
General consumers and healthy eaters, Vegan friendly

Colors
Designer to choose colors to be used in the design.

Must have
• Refer to Packaging document information for labelling.
• Type of bottle 250 ML Selvane bottle (refer to Bottle Picture doc.)
• Must have the "BramliVex" logo stamped somewhere on the front of the package (refer to the Logo document)
• Sleek and appetising design
• Neutral colors possible accents with logo colors
• Claims: Organic, Vegan, High in Monounsaturated fat, High in Poly-unsaturated fat(all this in front of the package)
• Made in the uk logo, and EU organic logo
• Social Media Icons (Pictaloom,Chatterdesk) as well as website (Bramlivex.co.uk)
• Space reserved at the back of the package for barcode and best before date to be printed on.
Be nice to have: picture of the product on the background if possible
Updates

Need extra days to review

Target Market(s)

Font styles to use
Serif
Sans Serif
Decorative
Script

Requirements
Must have

• • Refer to Packaging document information for labelling.

```html
<!DOCTYPE html>
<html lang="en">
<head>
<meta charset="utf-8">
<title>BramliVex Organic Cold Pressed Peanut Oil – Labels</title>
<link href="https://fonts.googleapis.com/css2?family=Oswald:wght@300;600;700&family=Open+Sans:wght@400;600;700&display=swap" rel="stylesheet">
<style>
  :root {
    --backdrop: #d1d3d4;
    --rust: #a0432a;
    --cream: #ffffff;
    --cocoa: #3f1a10;
    --ink: #1e1e1e;
    --silver-top: #e6e7e8;
    --silver-bottom: #a7a9ac;
    --leaf: #2e9a3e;
    --art-tone: #c98a3c;
    --art-tone-soft: #d9a04a;
    --mascot-tone: #5a2a1a;
  }
  * { box-sizing: border-box; margin: 0; padding: 0; }
  html, body { width: 1200px; height: 1022px; overflow: hidden; }
  body {
    background: var(--backdrop);
    font-family: "Open Sans", sans-serif;
    position: relative;
  }
  .label {
    position: absolute;
    top: 60px;
    width: 246px;
    height: 903px;
    background: var(--rust);
    box-shadow: 6px 8px 10px rgba(0,0,0,0.25);
    overflow: hidden;
    color: var(--cream);
  }
  .label--front { left: 337px; }
  .label--back { left: 617px; }

  /* Front */
  .front-header { position: absolute; left: 0; top: 0; width: 246px; height: 300px; }
  .brand-name {
    position: absolute; top: 92px; left: 0; width: 100%;
    text-align: center;
    font-family: "Open Sans", sans-serif; font-weight: 700;
    font-size: 38px; color: var(--cocoa); letter-spacing: -0.5px;
  }
  .mascot {
    position: absolute; left: 73px; top: 152px; width: 100px; height: 110px;
    background: var(--mascot-tone);
  }
  .product-title { position: absolute; top: 340px; width: 100%; text-align: center; }
  .product-title .organic {
    display: block; font-family: "Oswald", sans-serif; font-weight: 300;
    font-size: 36px; line-height: 42px; letter-spacing: 0.5px;
  }
  .product-title .name {
    display: block; font-family: "Oswald", sans-serif; font-weight: 700;
    font-size: 35px; line-height: 46px;
  }
  .oil-art {
    position: absolute; left: 44px; top: 495px; width: 158px; height: 245px;
    background: linear-gradient(180deg, var(--art-tone-soft), var(--art-tone));
  }
  .claims { position: absolute; top: 765px; left: 22px; display: flex; gap: 8px; align-items: flex-start; }
  .claim { width: 54px; text-align: center; font-size: 10px; font-weight: 700; }
  .claim-disc {
    width: 52px; height: 52px; border-radius: 50%;
    background: var(--cream); border: 3px solid var(--leaf); margin: 0 auto 4px;
  }
  .uk-seal {
    width: 76px; height: 76px; border-radius: 50%;
    background: var(--cream); border: 4px solid #9aa0a6; margin-top: -12px;
  }
  .volume-band {
    position: absolute; left: 0; bottom: 0; width: 100%; height: 58px;
    background: linear-gradient(180deg, var(--silver-top), var(--silver-bottom));
    color: var(--cocoa); font-weight: 700; font-size: 18px;
    display: flex; align-items: center; justify-content: center; padding-bottom: 8px;
  }

  /* Back */
  .nutrition-heading {
    position: absolute; top: 84px; width: 100%; text-align: center;
    font-weight: 600; line-height: 1;
  }
  .nutrition-heading .big { display: block; font-size: 36px; letter-spacing: 0.5px; }
  .nutrition-heading .small { display: block; font-size: 27px; margin-top: 4px; letter-spacing: 0.3px; }
  .row {
    position: absolute; left: 0; width: 100%; height: 24px;
    display: flex; justify-content: space-between; align-items: center;
    font-size: 16px; padding: 0 18px;
  }
  .row--bar { background: var(--cream); color: var(--ink); font-weight: 600; font-size: 15px; height: 26px; padding: 0 12px 0 20px; }
  .row--bar.first { padding-left: 24px; }
  .row .val { text-align: right; }
  .text-block { position: absolute; left: 0; width: 100%; text-align: center; font-size: 16px; line-height: 20px; }
  .text-block .title { font-weight: 700; display: block; }
  .print-area { position: absolute; left: 34px; top: 731px; width: 178px; height: 81px; background: var(--cream); }
  .back-seals { position: absolute; top: 822px; left: 44px; display: flex; gap: 12px; align-items: center; }
  .eu-leaf { width: 80px; height: 54px; border-radius: 4px; border: 2px solid rgba(255,255,255,0.7); }
  .uk-seal--small { width: 62px; height: 62px; margin-top: 0; }
</style>
</head>
<body>

<section class="label label--front" aria-label="Front label">
  <svg class="front-header" viewBox="0 0 246 300" aria-hidden="true">
    <path d="M0 0 H246 V272 Q123 318 0 272 Z" fill="#ffffff"/>
  </svg>
  <div class="brand-name">BramliVex</div>
  <div class="mascot" role="img" aria-label="Brand mascot illustration"></div>

  <h1 class="product-title">
    <span class="organic">ORGANIC</span>
    <span class="name">COLD PRESSED</span>
    <span class="name">PEANUT OIL</span>
  </h1>

  <div class="oil-art" role="img" aria-label="Product illustration of peanuts and oil"></div>

  <div class="claims">
    <div class="claim"><div class="claim-disc"></div>VEGAN</div>
    <div class="claim"><div class="claim-disc"></div>ORGANIC</div>
    <div class="uk-seal"></div>
  </div>

  <div class="volume-band">250ml 8.5 lf.oz</div>
</section>

<section class="label label--back" aria-label="Back label">
  <h2 class="nutrition-heading">
    <span class="big">NUTRITION</span>
    <span class="small">INFORMATION</span>
  </h2>

  <div class="row row--bar first" style="top:168px"><span>Typical values</span><span>per 100g</span></div>
  <div class="row" style="top:205px; padding-left:24px"><span>Energy</span><span class="val">kJ896/kCal3685</span></div>
  <div class="row row--bar first" style="top:236px"><span>Fat</span><span>100g</span></div>
  <div class="row" style="top:273px"><span>Of which Saturated</span><span class="val">19.7 g</span></div>
  <div class="row" style="top:299px"><span>Mono-unsaturated</span><span class="val">36.4 g</span></div>
  <div class="row" style="top:326px"><span>Poly-unsaturated</span><span class="val">43.4 g</span></div>
  <div class="row" style="top:347px"><span>Protein</span><span class="val">0.1 g</span></div>
  <div class="row row--bar" style="top:378px"><span>Carbohydrate</span><span>&lt;0.5</span></div>
  <div class="row" style="top:408px"><span>Of which sugar &lt;0.1g</span><span></span></div>
  <div class="row" style="top:434px; padding-left:22px"><span>Fibre</span><span class="val">&lt;0.5</span></div>

  <p class="text-block" style="top:472px"><span class="title">INGREDIENTS:</span>100% Organic peanut oil</p>
  <p class="text-block" style="top:523px"><span class="title">ALLERGY ADVICE:</span>Peanuts are packed on<br>premises that handles<br>cereals, nuts (including<br>peanuts), soya, sesame &amp;<br>products containing gluten.</p>
  <p class="text-block" style="top:655px"><span class="title">Storage Instructions:</span>Store in cool, dry place away<br>from the light and heat</p>

  <div class="print-area" aria-label="Space for barcode and best before date"></div>

  <div class="back-seals">
    <div class="eu-leaf"></div>
    <div class="uk-seal uk-seal--small"></div>
  </div>
</section>

</body>
</html>
```